Label design needed for cafe display

Hi,
We need a label designed so that we can label food in our display fridge.
The label would have to be editable, as we have lot's of different food items.. and we change the items often, so I would be constantly updating the labels. I will then be printing each label, and laminating them, then displaying them in our food display fridge.
We would like the label to contain our logo - which I have attached.
I have also attached our menus, so you can get a feel for the designs we like.
An example of what we need on a label:
QUICHE LORRAINE $7.50
With Salad $9.50
Please feel free to ask me any questions.
Printing

```html
<!DOCTYPE html>
<html lang="en">
<head>
<meta charset="utf-8">
<title>Good Measure – Display Fridge Label</title>
<link rel="stylesheet" href="https://fonts.googleapis.com/css2?family=Poiret+One&display=swap">
<style>
  :root {
    --label-yellow: #fdfca8;
    --band-black: #000000;
    --band-edge: #1c1c14;
    --ink-yellow: #f9f6a2;
    --logo-brown: #3f3233;
    --logo-ink: #f2eee8;
    --ornament-tone: #d9d68c;
  }
  * { margin: 0; padding: 0; box-sizing: border-box; }
  html, body {
    width: 1200px;
    height: 840px;
    overflow: hidden;
    background: var(--label-yellow);
  }
  .label {
    position: relative;
    width: 1200px;
    height: 840px;
    background: var(--label-yellow);
    font-family: "Poiret One", sans-serif;
  }
  .brand-mark {
    position: absolute;
    left: 524px;
    top: 30px;
    width: 184px;
    height: 184px;
    border-radius: 50%;
    background: var(--logo-brown);
    display: flex;
    flex-direction: column;
    align-items: center;
    justify-content: center;
    color: var(--logo-ink);
    font-size: 25px;
    letter-spacing: 2px;
    line-height: 1.15;
    text-align: center;
  }
  .ornament {
    position: absolute;
    background: var(--ornament-tone);
    border-radius: 40px;
  }
  .ornament--top-left     { left: 102px; top: 92px;  width: 360px; height: 50px; }
  .ornament--top-right    { left: 768px; top: 92px;  width: 366px; height: 50px; }
  .ornament--bottom-left  { left: 258px; top: 762px; width: 330px; height: 44px; }
  .ornament--bottom-right { left: 672px; top: 762px; width: 342px; height: 44px; }

  .price-band {
    position: absolute;
    left: 0;
    top: 246px;
    width: 1200px;
    height: 486px;
    background: var(--band-black);
  }
  .band-edge {
    position: absolute;
    left: 0;
    width: 1200px;
    height: 46px;
    background: var(--band-edge);
  }
  .band-edge--top    { top: 0; }
  .band-edge--bottom { bottom: 0; }

  .side-scroll {
    position: absolute;
    top: 72px;
    width: 46px;
    height: 354px;
    background: var(--ornament-tone);
    border-radius: 23px;
  }
  .side-scroll--left  { left: 46px; }
  .side-scroll--right { left: 1106px; }

  .item {
    position: absolute;
    left: 0;
    width: 1200px;
    text-align: center;
    color: var(--ink-yellow);
    font-size: 92px;
    line-height: 1;
    white-space: nowrap;
  }
  .item__name  { top: 160px; letter-spacing: 1px; }
  .item__extra { top: 278px; }
</style>
</head>
<body>
  <main class="label">
    <div class="brand-mark">
      <span>GOOD</span>
      <span>MEASURE</span>
    </div>

    <div class="ornament ornament--top-left" role="img" aria-label="Curled flourish ornament"></div>
    <div class="ornament ornament--top-right" role="img" aria-label="Curled flourish ornament"></div>

    <section class="price-band">
      <div class="band-edge band-edge--top" role="img" aria-label="Scalloped decorative border"></div>
      <div class="band-edge band-edge--bottom" role="img" aria-label="Scalloped decorative border"></div>
      <div class="side-scroll side-scroll--left" role="img" aria-label="Vertical scroll ornament"></div>
      <div class="side-scroll side-scroll--right" role="img" aria-label="Vertical scroll ornament"></div>

      <h1 class="item item__name">QUICHE LORRAINE $7.50</h1>
      <p class="item item__extra">With Salad $9.50</p>
    </section>

    <div class="ornament ornament--bottom-left" role="img" aria-label="Curled flourish ornament"></div>
    <div class="ornament ornament--bottom-right" role="img" aria-label="Curled flourish ornament"></div>
  </main>
</body>
</html>
```